Velmint website

A clean uncluttered design that shows at glance that we are in the Media and design and publishing business.

We would like to see designs that use colours that show warmth and quality.

The website should show:
- products
- projects

These should be displaxed in spaces that we can add or interchanges with new products or projects.
Updates

Target Market(s)

Business and project managers and buyers and authors.

Industry/Entity Type

Business

Requirements
Must have
• Good colours. Not too strong, not weak, but reflecting quality.

```html
<!DOCTYPE html>
<html lang="en">
<head>
<meta charset="utf-8">
<title>Velmint</title>
<link href="https://fonts.googleapis.com/css2?family=Open+Sans:wght@300;400&display=swap" rel="stylesheet">
<style>
  :root {
    --white: #ffffff;
    --ink: #2b2622;
    --muted: #7a716a;
    --nav: #6e655d;
    --rule: #e2dcd4;
    --hero-edge: #3d3630;
    --hero-dark: #8a7f73;
    --hero-light: #b3a796;
    --photo-light: #ece6de;
    --photo-dark: #cdc1b1;
  }
  * { margin: 0; padding: 0; box-sizing: border-box; }
  html, body {
    width: 1200px; height: 900px; overflow: hidden;
    background: var(--white);
    font-family: "Open Sans", Arial, sans-serif;
  }
  body { position: relative; }
  .site-header {
    position: absolute; top: 0; left: 0; width: 1200px; height: 42px;
    border-bottom: 1px solid var(--rule);
    background: var(--white);
  }
  .brand {
    position: absolute; left: 60px; top: 8px;
    font-size: 18px; font-weight: 300; line-height: 24px; color: var(--ink);
  }
  .main-nav {
    position: absolute; right: 60px; top: 15px;
    display: flex; gap: 29px;
    list-style: none;
  }
  .main-nav li {
    font-size: 8px; font-weight: 400; line-height: 11px; color: var(--nav);
  }
  .hero {
    position: absolute; top: 42px; left: 0; width: 1200px; height: 533px;
    background: linear-gradient(110deg, var(--hero-dark) 0%, var(--hero-light) 100%);
    border-bottom: 1px solid var(--hero-edge);
  }
  .hero-title {
    position: absolute; top: 186px; left: 0; width: 100%; text-align: center;
    font-size: 35px; font-weight: 300; line-height: 46px; color: var(--white);
    letter-spacing: 6.4px;
  }
  .hero-button {
    position: absolute; left: 523px; top: 261px; width: 152px; height: 40px;
    border: 1px solid var(--white);
    color: var(--white); font-size: 10px; letter-spacing: 2px;
    display: flex; align-items: center; justify-content: center;
  }
  .slider-arrow { position: absolute; top: 230px; }
  .slider-arrow.prev { left: 211px; }
  .slider-arrow.next { left: 972px; }
  .about {
    position: absolute; top: 576px; left: 0; width: 1200px; height: 324px;
    overflow: hidden; text-align: center;
  }
  .section-title {
    position: absolute; top: 60px; left: 0; width: 100%;
    font-size: 25px; font-weight: 300; line-height: 34px; color: var(--ink);
    letter-spacing: 4px;
  }
  .section-rule {
    position: absolute; top: 104px; left: 573px;
    width: 52px; height: 2px; background: var(--ink);
  }
  .section-lead {
    position: absolute; top: 138px; left: 0; width: 100%;
    font-size: 10px; line-height: 14px; color: var(--muted);
  }
  .about-photo {
    position: absolute; top: 184px; left: 287px; width: 624px; height: 140px;
    background: linear-gradient(120deg, var(--photo-light) 0%, var(--photo-dark) 100%);
  }
</style>
</head>
<body>
  <header class="site-header">
    <div class="brand">Velmint</div>
    <ul class="main-nav">
      <li>HOME</li>
      <li>ABOUT</li>
      <li>SERVICES</li>
      <li>FOLIO</li>
      <li>TEAM</li>
      <li>CONTACT US</li>
    </ul>
  </header>

  <section class="hero" role="img" aria-label="Featured project slide, warm textured photograph of a publishing project">
    <h1 class="hero-title">CREATIVE DESIGN.</h1>
    <div class="hero-button">LEARN MORE</div>
    <svg class="slider-arrow prev" width="16" height="32" viewBox="0 0 16 32" aria-hidden="true">
      <polyline points="14,1 2,16 14,31" fill="none" stroke="#ffffff" stroke-width="1"/>
    </svg>
    <svg class="slider-arrow next" width="16" height="32" viewBox="0 0 16 32" aria-hidden="true">
      <polyline points="2,1 14,16 2,31" fill="none" stroke="#ffffff" stroke-width="1"/>
    </svg>
  </section>

  <section class="about">
    <h2 class="section-title">ABOUT US</h2>
    <div class="section-rule"></div>
    <p class="section-lead">Here your description</p>
    <div class="about-photo" role="img" aria-label="Photograph of the studio's printed products"></div>
  </section>
</body>
</html>
```